IT Services Company - Company Logo, Flyer design

We are an IT professional services company that provides technical service and support in the residential market. I would like to create a colorful logo and flyer that will be mainly letterbox dropped.

Target Market(s)

residential

Industry/Entity Type

It Company

Requirements
Must have
• nice look and feel, easy to read

```html
<!DOCTYPE html>
<html lang="en">
<head>
<meta charset="utf-8">
<title>Airwave Communications – IT Services Flyer</title>
<link href="https://fonts.googleapis.com/css2?family=Roboto+Condensed:wght@400;700&display=swap" rel="stylesheet">
<style>
  :root {
    --page-bg: #161618;
    --flyer-top: #17181c;
    --flyer-mid: #24252e;
    --violet-deep: #3a2f78;
    --pill: #2c278e;
    --ink: #ffffff;
    --ink-soft: #d6d4ea;
  }
  * { margin: 0; padding: 0; box-sizing: border-box; }
  html, body { width: 1200px; height: 1200px; overflow: hidden; background: var(--page-bg); }
  body { font-family: "Roboto Condensed", sans-serif; color: var(--ink); }

  .flyer {
    position: absolute; left: 136px; top: 0; width: 928px; height: 1200px;
    background: linear-gradient(180deg, var(--flyer-top) 0%, var(--flyer-mid) 55%, #2c2d3a 100%);
    overflow: hidden;
  }
  .hero-visual {
    position: absolute; left: 494px; top: 150px; width: 434px; height: 420px;
    background: radial-gradient(ellipse at 45% 55%, rgba(170,210,255,.85) 0%, rgba(63,143,214,.55) 25%, rgba(40,70,130,.35) 50%, rgba(23,24,28,0) 75%);
  }
  .brand-name, .brand-sub { position: absolute; left: 50px; font-weight: 700; line-height: 1; white-space: nowrap; }
  .brand-name { top: 150px; font-size: 135px; letter-spacing: -2px; }
  .brand-sub { top: 271px; font-size: 68px; letter-spacing: -1px; }
  .tagline { position: absolute; left: 52px; top: 345px; font-size: 25px; line-height: 33px; color: var(--ink-soft); white-space: nowrap; }

  .services-bg { position: absolute; left: 0; top: 579px; width: 928px; height: 621px; }
  .services { position: absolute; list-style: none; font-size: 18.5px; line-height: 25px; white-space: nowrap; }
  .services li { position: relative; padding-left: 37px; margin-bottom: 8px; }
  .services li svg { position: absolute; left: 0; top: 3px; }
  .services-left { left: 51px; top: 609px; }
  .services-right { left: 486px; top: 609px; }

  .rate { position: absolute; left: 44px; top: 934px; width: 230px; text-align: center; font-weight: 700; font-size: 40px; line-height: 44px; white-space: nowrap; }
  .rate-divider { position: absolute; left: 284px; top: 944px; width: 1px; height: 106px; background: rgba(255,255,255,.35); }
  .price { position: absolute; left: 306px; top: 942px; font-weight: 700; font-size: 100px; line-height: 1; letter-spacing: -1px; }
  .cards-pill {
    position: absolute; left: 52px; top: 1086px; width: 391px; height: 45px; border-radius: 23px;
    background: var(--pill); font-size: 29px; line-height: 45px; text-align: center; white-space: nowrap;
  }
  .procure { position: absolute; left: 463px; top: 927px; width: 465px; text-align: center; font-size: 37px; line-height: 44px; white-space: nowrap; }
  .contact { position: absolute; left: 463px; top: 1087px; width: 465px; height: 113px; background: var(--violet-deep); text-align: center; }
  .contact-phone { font-size: 25px; line-height: 30px; margin-top: 13px; }
  .contact-web { font-size: 13.5px; margin-top: 4px; }
</style>
</head>
<body>
<main class="flyer">
  <div class="hero-visual" role="img" aria-label="Hand holding a glowing laptop surrounded by floating email, network and world map icons"></div>

  <header>
    <h1 class="brand-name">Airwave</h1>
    <p class="brand-sub">Communications</p>
  </header>
  <p class="tagline">We are an IT Professional Services Company<br>That Provides Technical Service And Support</p>

  <svg class="services-bg" viewBox="0 0 928 621" width="928" height="621" aria-hidden="true">
    <defs>
      <linearGradient id="leftPanel" x1="0" y1="0" x2="0" y2="1">
        <stop offset="0" stop-color="#4a4775"/>
        <stop offset="1" stop-color="#4b3990"/>
      </linearGradient>
      <linearGradient id="rightPanel" x1="0" y1="0" x2="0" y2="1">
        <stop offset="0" stop-color="#3c3d52" stop-opacity=".6"/>
        <stop offset="1" stop-color="#5b6070" stop-opacity=".8"/>
      </linearGradient>
    </defs>
    <polygon points="0,0 390,0 463,35 463,621 0,621" fill="url(#leftPanel)"/>
    <rect x="463" y="0" width="465" height="339" fill="url(#rightPanel)"/>
    <polygon points="463,339 880,339 928,300 928,508 463,508" fill="#4c4793"/>
  </svg>

  <ul class="services services-left">
    <li><svg width="20" height="20" viewBox="0 0 20 20"><rect x="1" y="3" width="15" height="15" fill="none" stroke="#fff" stroke-width="2"/><path d="M5 10l4 4 9-11" fill="none" stroke="#fff" stroke-width="2"/></svg>Home Network &amp; Wireless setup</li>
    <li><svg width="20" height="20" viewBox="0 0 20 20"><rect x="1" y="3" width="15" height="15" fill="none" stroke="#fff" stroke-width="2"/><path d="M5 10l4 4 9-11" fill="none" stroke="#fff" stroke-width="2"/></svg>Improvements for extending your home Wireless</li>
    <li><svg width="20" height="20" viewBox="0 0 20 20"><rect x="1" y="3" width="15" height="15" fill="none" stroke="#fff" stroke-width="2"/><path d="M5 10l4 4 9-11" fill="none" stroke="#fff" stroke-width="2"/></svg>IP Camera installations – external and internal</li>
    <li><svg width="20" height="20" viewBox="0 0 20 20"><rect x="1" y="3" width="15" height="15" fill="none" stroke="#fff" stroke-width="2"/><path d="M5 10l4 4 9-11" fill="none" stroke="#fff" stroke-width="2"/></svg>Backup solutions either at home or<br>to a cloud provider</li>
    <li><svg width="20" height="20" viewBox="0 0 20 20"><rect x="1" y="3" width="15" height="15" fill="none" stroke="#fff" stroke-width="2"/><path d="M5 10l4 4 9-11" fill="none" stroke="#fff" stroke-width="2"/></svg>Computer &amp; Network Security</li>
    <li><svg width="20" height="20" viewBox="0 0 20 20"><rect x="1" y="3" width="15" height="15" fill="none" stroke="#fff" stroke-width="2"/><path d="M5 10l4 4 9-11" fill="none" stroke="#fff" stroke-width="2"/></svg>Email setup</li>
    <li><svg width="20" height="20" viewBox="0 0 20 20"><rect x="1" y="3" width="15" height="15" fill="none" stroke="#fff" stroke-width="2"/><path d="M5 10l4 4 9-11" fill="none" stroke="#fff" stroke-width="2"/></svg>Domain setup and email migration to cloud</li>
  </ul>

  <ul class="services services-right">
    <li><svg width="20" height="20" viewBox="0 0 20 20"><rect x="1" y="3" width="15" height="15" fill="none" stroke="#fff" stroke-width="2"/><path d="M5 10l4 4 9-11" fill="none" stroke="#fff" stroke-width="2"/></svg>Streaming stick installations and wireless setup-<br>Stream movies and shows to your existing TV</li>
    <li><svg width="20" height="20" viewBox="0 0 20 20"><rect x="1" y="3" width="15" height="15" fill="none" stroke="#fff" stroke-width="2"/><path d="M5 10l4 4 9-11" fill="none" stroke="#fff" stroke-width="2"/></svg>Computer Setup</li>
    <li><svg width="20" height="20" viewBox="0 0 20 20"><rect x="1" y="3" width="15" height="15" fill="none" stroke="#fff" stroke-width="2"/><path d="M5 10l4 4 9-11" fill="none" stroke="#fff" stroke-width="2"/></svg>New computer recommendations</li>
    <li><svg width="20" height="20" viewBox="0 0 20 20"><rect x="1" y="3" width="15" height="15" fill="none" stroke="#fff" stroke-width="2"/><path d="M5 10l4 4 9-11" fill="none" stroke="#fff" stroke-width="2"/></svg>New computer unpacking and setup</li>
    <li><svg width="20" height="20" viewBox="0 0 20 20"><rect x="1" y="3" width="15" height="15" fill="none" stroke="#fff" stroke-width="2"/><path d="M5 10l4 4 9-11" fill="none" stroke="#fff" stroke-width="2"/></svg>Mobile phone setups and training</li>
    <li><svg width="20" height="20" viewBox="0 0 20 20"><rect x="1" y="3" width="15" height="15" fill="none" stroke="#fff" stroke-width="2"/><path d="M5 10l4 4 9-11" fill="none" stroke="#fff" stroke-width="2"/></svg>Computer training</li>
    <li><svg width="20" height="20" viewBox="0 0 20 20"><rect x="1" y="3" width="15" height="15" fill="none" stroke="#fff" stroke-width="2"/><path d="M5 10l4 4 9-11" fill="none" stroke="#fff" stroke-width="2"/></svg>Telephony &amp; Network Cable relations<br>and installations</li>
  </ul>

  <p class="rate">WE CHARGE<br>Ex Gst<br>Per Hour</p>
  <div class="rate-divider"></div>
  <p class="price">$70</p>
  <p class="cards-pill">All major credit cards accepted</p>

  <p class="procure">We Can Procure All New<br>Hardware And Provide You<br>Obligation Free Quotes.</p>

  <footer class="contact">
    <p class="contact-phone">PH : 0000000</p>
    <p class="contact-web">hello@airwavecomms.com &nbsp;|&nbsp; www.airwavecomms.com</p>
  </footer>
</main>
</body>
</html>
```